VORELL Pathology

I have a website on vorellpathology.webnestly.com which I need further customized. This is a pathology/laboratory website. an example of my previous website is at quenbypath.com. We provide expertise in Dermatopathology & Anatomic Pathology to the Physicians & Patients since 2010.

Target Market(s)

Other medical professionals/doctors

Industry/Entity Type

Pathology, laboratory, medical doctor

Coding

Coded - Design and coding required

Number of Pages Required

4 page

Font styles to use
Serif
Sans Serif

Colors

Designer to choose colors to be used in the design.

Requirements
Must have
• Clean modern design, easy navigation

```html
<!DOCTYPE html>
<html lang="en">
<head>
<meta charset="utf-8">
<title>VORELL Pathology</title>
<link href="https://fonts.googleapis.com/css2?family=Roboto:wght@300;400;500;700&display=swap" rel="stylesheet">
<style>
:root{
  --purple:#5a23b5;
  --purple-band:#5f2bb0;
  --blue:#1e6fc0;
  --blue-band:#2376c8;
  --ink:#111;
  --text:#444;
  --muted:#666;
  --paper:#fff;
  --mist:#eef5f7;
  --footer:#0b0b0c;
}
*{box-sizing:border-box;margin:0;padding:0}
html,body{width:1200px;height:3900px;overflow:hidden}
body{font-family:"Roboto",Arial,sans-serif;color:var(--ink);background:var(--mist);position:relative}
.abs{position:absolute}
a{color:inherit;text-decoration:none}

/* header */
.site-header{position:absolute;left:0;top:0;width:1200px;height:112px;background:var(--paper);box-shadow:0 2px 6px rgba(0,0,0,.08);z-index:2}
.brand{position:absolute;left:110px;top:20px;display:flex;align-items:center;gap:14px}
.brand-dot{width:70px;height:70px;border-radius:50%;border:5px solid var(--purple);flex:none}
.brand-name{font-size:36px;font-weight:700;color:var(--purple);letter-spacing:.5px;line-height:1;white-space:nowrap}
.callbox{position:absolute;left:702px;top:13px;display:flex;align-items:center;gap:8px}
.round{width:42px;height:42px;border-radius:50%;border:2px solid var(--purple);display:flex;align-items:center;justify-content:center}
.callbox small{display:block;font-size:12px;font-weight:500}
.callbox strong{font-size:17px;font-weight:500}
.socials{position:absolute;left:895px;top:13px;display:flex;gap:8px}
.socials span{width:44px;height:44px;border-radius:50%;border:2px solid var(--purple);display:flex;align-items:center;justify-content:center}
.main-nav{position:absolute;right:113px;top:77px;display:flex;gap:30px;font-size:15px;font-weight:500}
.main-nav a.active{color:var(--purple)}

/* hero */
.hero{position:absolute;left:0;top:112px;width:1200px;height:569px;background:linear-gradient(100deg,#1d4fa3 0%,#3c79d1 40%,#8db8ea 62%,#2b55a0 85%,#0e2a62 100%)}
.hero-title{position:absolute;left:110px;top:158px;font-size:45px;font-weight:700;color:#fff;line-height:46px}
.hero-text{position:absolute;left:110px;top:250px;width:540px;font-size:19px;line-height:32px;color:#fff;font-weight:500}
.btn-solid{display:inline-flex;align-items:center;justify-content:center;background:var(--purple);color:#fff;border-radius:30px;font-weight:500;font-size:15px}
.hero .btn-solid{position:absolute;left:110px;top:367px;width:172px;height:52px}
.hero-arrow{position:absolute;top:265px}
.dots{position:absolute;left:562px;top:519px;display:flex;gap:9px}
.dots i{width:12px;height:12px;border-radius:50%;background:rgba(255,255,255,.5)}
.dots i:first-child{background:#fff}

/* about */
.about-photo{left:110px;top:763px;width:463px;height:375px;background:linear-gradient(160deg,#3a4d63,#1d2a3a)}
.section-copy{position:absolute;left:635px;width:455px}
.section-copy h2{font-size:36px;font-weight:500;margin-bottom:24px}
.section-copy p{font-size:13px;line-height:28px;color:var(--text);margin-bottom:10px}
.btn-ghost{display:inline-flex;align-items:center;justify-content:center;border:2px solid var(--purple);color:var(--purple);border-radius:30px;font-weight:500;font-size:15px;height:52px}

/* services */
.services-band{left:0;top:1226px;width:1200px;height:426px;background:linear-gradient(180deg,var(--blue) 0%,var(--blue-band) 100%)}
.center-head{position:absolute;left:0;width:1200px;text-align:center}
.services-head h2{font-size:34px;font-weight:500;color:#fff}
.services-head p{font-size:15px;line-height:25px;color:#fff;margin-top:16px}
.card{position:absolute;background:var(--paper);box-shadow:0 3px 10px rgba(0,0,0,.1);text-align:center}
.card .media{margin:8px;height:213px}
.card h3{font-size:21px;font-weight:500;margin-top:18px}
.card p{font-size:12px;line-height:26px;color:var(--muted);padding:10px 16px 0}
.card .more{display:inline-block;margin-top:8px;font-size:13px;font-weight:700;color:var(--purple);text-decoration:underline}
.circle-arrow{position:absolute;width:28px;height:28px;border-radius:50%;border:1.5px solid #fff;display:flex;align-items:center;justify-content:center}

/* blog */
.blog-band{left:0;top:2391px;width:1200px;height:396px;background:var(--purple-band)}
.blog-card{position:absolute;top:2584px;width:314px;height:406px;background:var(--paper);box-shadow:0 3px 10px rgba(0,0,0,.1)}
.blog-card .media{margin:5px;height:218px}
.blog-card h3{font-size:16px;font-weight:500;line-height:21px;padding:14px 10px 0}
.blog-card p{font-size:12px;line-height:22px;color:var(--muted);padding:10px 10px 0}
.blog-card .more{display:block;padding:10px 10px 0;font-size:14px;font-weight:700;color:var(--purple)}

/* contact */
.field{position:absolute;background:var(--paper);font-size:14px;color:#555;padding:18px 17px}

/* footer */
.site-footer{left:0;top:3580px;width:1200px;height:320px;background:var(--footer);color:#fff}
.footer-brand{top:54px;gap:12px}
.footer-brand .brand-dot{border-color:#fff;width:62px;height:62px;border-width:4px}
.footer-brand .brand-name{color:#fff;font-size:26px}
.foot-col{position:absolute;top:58px}
.foot-col h4{font-size:19px;font-weight:500;margin-bottom:14px}
.foot-col li{list-style:none;font-size:13px;line-height:26px}
.foot-contact li{display:flex;gap:12px;align-items:flex-start;margin-bottom:10px;line-height:20px}
.foot-social{position:absolute;left:162px;top:175px;display:flex;gap:6px}
.foot-social span{width:34px;height:34px;border-radius:50%;border:1.5px solid #fff;display:flex;align-items:center;justify-content:center}
.copyright{position:absolute;left:0;bottom:12px;width:1200px;text-align:center;font-size:13px}
</style>
</head>
<body>

<header class="site-header">
  <div class="brand"><span class="brand-dot"></span><span class="brand-name">VORELL Pathology</span></div>
  <div class="callbox">
    <span class="round"><svg width="20" height="20" viewBox="0 0 24 24" fill="none" stroke="#5a23b5" stroke-width="2"><path d="M5 3h4l2 5-2.5 1.5a11 11 0 0 0 6 6L16 13l5 2v4a2 2 0 0 1-2 2A16 16 0 0 1 3 5a2 2 0 0 1 2-2z"/></svg></span>
    <div><small>CALL US:</small><strong>(970) 555-0142</strong></div>
  </div>
  <div class="socials" aria-label="Social links">
    <span><svg width="18" height="18" viewBox="0 0 24 24" fill="none" stroke="#5a23b5" stroke-width="2"><circle cx="12" cy="12" r="9"/><path d="M3 12h18M12 3c3 3 3 15 0 18M12 3c-3 3-3 15 0 18"/></svg></span>
    <span><svg width="18" height="18" viewBox="0 0 24 24" fill="none" stroke="#5a23b5" stroke-width="2"><path d="M4 5h16v11H9l-5 4z"/></svg></span>
    <span><svg width="18" height="18" viewBox="0 0 24 24" fill="none" stroke="#5a23b5" stroke-width="2"><circle cx="12" cy="8" r="4"/><path d="M4 21c1-5 15-5 16 0"/></svg></span>
    <span><svg width="18" height="18" viewBox="0 0 24 24" fill="none" stroke="#5a23b5" stroke-width="2"><path d="M10 14a4 4 0 0 0 6 0l3-3a4 4 0 0 0-6-6l-1 1M14 10a4 4 0 0 0-6 0l-3 3a4 4 0 0 0 6 6l1-1"/></svg></span>
  </div>
  <nav class="main-nav">
    <a class="active" href="#">HOME</a><a href="#">EXCEPTIONAL PATHOLOGY</a><a href="#">ABOUT US</a><a href="#">FORMS</a><a href="#">CONTACT US</a>
  </nav>
</header>

<section class="hero" role="img" aria-label="Laboratory microscope in blue light">
  <svg class="hero-arrow" style="left:68px" width="28" height="54" viewBox="0 0 28 54"><path d="M26 2 2 27l24 25" fill="none" stroke="#fff" stroke-width="2"/></svg>
  <svg class="hero-arrow" style="left:1100px" width="28" height="54" viewBox="0 0 28 54"><path d="M2 2l24 25L2 52" fill="none" stroke="#fff" stroke-width="2"/></svg>
  <h1 class="hero-title">EXCEPTIONAL PATHOLOGY<br>SERVICES</h1>
  <p class="hero-text">Our promise to you: a high level of accessibility, personalized physician consultation, as well as accurate, clear and prompt diagnoses.</p>
  <a class="btn-solid" href="#">GET STARTED</a>
  <div class="dots"><i></i><i></i><i></i><i></i></div>
</section>

<div class="abs about-photo" role="img" aria-label="Portrait of Dr. Halvern"></div>
<div class="section-copy" style="top:752px">
  <h2>ABOUT US</h2>
  <p>Dr. Halvern is board certified in Dermatopathology and Anatomic Pathology. In addition, Dr. Halvern is fellowship trained in Surgical Pathology.</p>
  <p>Dr. Halvern grew up in southern California and received her Bachelor of Science degree in Microbiology from Westmere University, Linden College of Science and Engineering. She earned her medical degree and was elected to the Sigma Caduceus Medical Honor Society at Harbourton University. Dr. Halvern then completed her residency in Anatomic Pathology at Ashgrove University, followed by intensive</p>
  <a class="btn-ghost" href="#" style="width:246px;margin-top:30px">KNOW MORE ABOUT US</a>
</div>

<div class="abs services-band"></div>
<div class="center-head services-head" style="top:1286px">
  <h2>OUR SERVICES</h2>
  <p>Sed ut perspiciatis unde omnis iste natus error sit voluptatem accusantium doloremque<br>laudantium, totam rem aperiam, eaque ipsa</p>
</div>
<span class="circle-arrow" style="left:58px;top:1598px"><svg width="10" height="12" viewBox="0 0 10 12"><path d="M7 1 2 6l5 5" fill="none" stroke="#fff" stroke-width="1.5"/></svg></span>
<span class="circle-arrow" style="left:1109px;top:1574px"><svg width="10" height="12" viewBox="0 0 10 12"><path d="M3 1l5 5-5 5" fill="none" stroke="#fff" stroke-width="1.5"/></svg></span>

<article class="card" style="left:110px;top:1430px;width:314px;height:404px">
  <div class="media" role="img" aria-label="Eye examination at a slit lamp" style="background:linear-gradient(135deg,#d9d6d2,#b9b3ad)"></div>
  <h3>OPHTHALMIC PATHOLOGY</h3>
  <p>Lorem ipsum dolor sit amet, consctetur adipiscing elit, sed do eiusmod tempor incididunt ut labore et dolore magna aliqua. Quis ipsum</p>
  <a class="more" href="#">READ MORE</a>
</article>
<article class="card" style="left:442px;top:1430px;width:314px;height:404px">
  <div class="media" role="img" aria-label="Clinician dressing a patient's knee wound" style="background:linear-gradient(135deg,#d8d3cf,#9a9088)"></div>
  <h3>WOUND PATHOLOGY</h3>
  <p>Lorem ipsum dolor sit amet, consctetur adipiscing elit, sed do eiusmod tempor incididunt ut labore et dolore magna aliqua. Quis ipsum</p>
  <a class="more" href="#">READ MORE</a>
</article>
<article class="card" style="left:773px;top:1430px;width:314px;height:404px">
  <div class="media" role="img" aria-label="Close-up of a smile with a pen pointing at teeth" style="background:linear-gradient(135deg,#e8c3b3,#c7877a)"></div>
  <h3>ORAL PATHOLOGY</h3>
  <p>Lorem ipsum dolor sit amet, consctetur adipiscing elit, sed do eiusmod tempor incididunt ut labore et dolore magna aliqua. Quis ipsum</p>
  <a class="more" href="#">READ MORE</a>
</article>

<div class="abs" role="img" aria-label="Microscope objective lens in blue light" style="left:110px;top:1928px;width:463px;height:375px;background:linear-gradient(135deg,#1a2fa0,#5a7ee0 45%,#c7d4f2 60%,#1c2f8e)"></div>
<div class="section-copy" style="top:1930px">
  <h2 style="font-size:26px;margin-bottom:22px">EXCEPTIONAL PATHOLOGY SERVICES</h2>
  <p>At VORELL Pathology, we strive to provide you with exceptional pathology services. We believe that strong consultative relationships lead to the best possible care for every patient.</p>
  <p style="margin:-6px 0 0;line-height:28px">Our promise to you includes:<br>• One-day turn around for the majority of cases<br>• Accurate, clear and detailed diagnostic reporting<br>• Clinicopathologic correlation<br>• Literature based sign-out</p>
  <a class="btn-ghost" href="#" style="width:172px;margin-top:40px">LEARN MORE</a>
</div>

<div class="abs blog-band"></div>
<div class="center-head" style="top:2480px;color:#fff">
  <p style="font-size:15px">News and Events</p>
  <h2 style="font-size:38px;font-weight:500;margin-top:8px">Our Blog &amp; Events</h2>
</div>

<article class="blog-card" style="left:110px">
  <div class="media" role="img" aria-label="Woman applying sunscreen outdoors" style="background:linear-gradient(180deg,#d7dde3,#7b6a62)"></div>
  <h3>SUNSCREEN 365: IT ISN'T JUST FOR SUMMER!</h3>
  <p>There are adroit in your order which keeps them updated on it becomes confusing for facts and submit it. Online marketing of any extra</p>
  <a class="more" href="#">READ MORE</a>
</article>
<article class="blog-card" style="left:442px">
  <div class="media" role="img" aria-label="Lab staff working at microscopes" style="background:linear-gradient(180deg,#eef1f4,#9fb0bf)"></div>
  <h3>WE'VE GOT YOUR NORTHFIELD REGIONAL HEALTH EMPLOYEES</h3>
  <p>We have received a lot of inquiries about whether or not we accept the new Northfield Regional Health (formerly Riverbend Valley Health System)</p>
  <a class="more" href="#">READ MORE</a>
</article>
<article class="blog-card" style="left:773px">
  <div class="media" role="img" aria-label="Awareness day illustration with a teal ribbon" style="background:linear-gradient(180deg,#1f8f94,#0f6a70)"></div>
  <h3>MAY IS MELANOMA/SKIN CANCER AWARENESS MONTH</h3>
  <p>It is currently estimated that one in five Americans will develop skin cancer in their lifetime. Numbers like that make a world without skin cancer</p>
  <a class="more" href="#">READ MORE</a>
</article>

<div class="center-head" style="top:3070px">
  <p style="font-size:15px;color:var(--blue)">Get Info</p>
  <h2 style="font-size:38px;font-weight:500;margin-top:8px">Get In Touch</h2>
</div>
<div class="field" style="left:238px;top:3167px;width:356px;height:53px">Full Name</div>
<div class="field" style="left:606px;top:3167px;width:356px;height:53px">Last Name</div>
<div class="field" style="left:238px;top:3231px;width:356px;height:53px">Email</div>
<div class="field" style="left:606px;top:3231px;width:356px;height:53px">Phone</div>
<div class="field" style="left:238px;top:3295px;width:724px;height:122px">Message</div>
<a class="btn-solid abs" href="#" style="left:485px;top:3436px;width:231px;height:53px">SUBMIT NOW</a>

<footer class="abs site-footer">
  <div class="brand footer-brand"><span class="brand-dot"></span><span class="brand-name">VORELL Pathology</span></div>
  <div class="foot-social" aria-label="Social links">
    <span><svg width="15" height="15" viewBox="0 0 24 24" fill="none" stroke="#fff" stroke-width="2"><circle cx="12" cy="12" r="9"/><path d="M3 12h18M12 3c3 3 3 15 0 18M12 3c-3 3-3 15 0 18"/></svg></span>
    <span><svg width="15" height="15" viewBox="0 0 24 24" fill="none" stroke="#fff" stroke-width="2"><path d="M4 5h16v11H9l-5 4z"/></svg></span>
    <span><svg width="15" height="15" viewBox="0 0 24 24" fill="none" stroke="#fff" stroke-width="2"><circle cx="12" cy="8" r="4"/><path d="M4 21c1-5 15-5 16 0"/></svg></span>
    <span><svg width="15" height="15" viewBox="0 0 24 24" fill="none" stroke="#fff" stroke-width="2"><path d="M10 14a4 4 0 0 0 6 0l3-3a4 4 0 0 0-6-6l-1 1M14 10a4 4 0 0 0-6 0l-3 3a4 4 0 0 0 6 6l1-1"/></svg></span>
  </div>
  <div class="foot-col" style="left:481px"><h4>COMPANY</h4><ul><li>Home</li><li>Exceptional Pathology</li><li>About Us</li><li>Forms</li><li>Contact Us</li></ul></div>
  <div class="foot-col" style="left:673px"><h4>RESOURCES</h4><ul><li>Support</li><li>Testimonials</li><li>Sitemap</li><li>Career</li><li>FAQ</li></ul></div>
  <div class="foot-col foot-contact" style="left:890px"><h4>CONTACT US</h4><ul>
    <li><svg width="16" height="20" viewBox="0 0 16 20" fill="none" stroke="#fff" stroke-width="1.5"><path d="M8 19s7-7 7-11A7 7 0 0 0 1 8c0 4 7 11 7 11z"/><circle cx="8" cy="8" r="2.5"/></svg><span>48 Elmwood Avenue, Castleford<br>10150, United States</span></li>
    <li><svg width="18" height="18" viewBox="0 0 24 24" fill="none" stroke="#fff" stroke-width="1.5"><path d="M5 3h4l2 5-2.5 1.5a11 11 0 0 0 6 6L16 13l5 2v4a2 2 0 0 1-2 2A16 16 0 0 1 3 5a2 2 0 0 1 2-2z"/></svg><span>970 . 555 . 0142</span></li>
    <li><svg width="20" height="16" viewBox="0 0 20 16" fill="none" stroke="#fff" stroke-width="1.5"><rect x="1" y="1" width="18" height="14"/><path d="M1 1l9 8 9-8"/></svg><span>info@quenbypath.com</span></li>
  </ul></div>
  <p class="copyright">Copyright © 2022 Vorell pathology. All Rights Reserved.</p>
</footer>

</body>
</html>
```